Stickers to put on my honeyglasses

Stickers for my honey glasses.
Only a single sticker on the front. Same should have a stripe on the top side which goes above the lid to show if the glass was opened.
Size of the main part should be 55mm high and max. 100 mm wide.
The stripe on the top should be 70mm long.
I added a Picture of another producer which uses the same glass as I do.
I should say: 'e Lendorf Glas Hunneg'. which means 'another glass of honey. 'Hunneg' should be mainly visible and therefore very large. 'e Lendorf Glas' should be less visible and therefore smaller above the 'Hunneg'
- It needs to contain the quantity : '500gr'
- It needs to contain my Name and address: 'Marc Lendorf, 38, rue Ferd Lusang, L-9241 Miersch' (This should be small and not to visible)
- It needs to conatin a validity Line: ´Am beschte virum:` (With enough space so I can add a date by hand)
- It needs to say: 'dréchen, kill andäischterstockéieren' (to store it dry cold and dark)

```html
<!DOCTYPE html>
<html lang="lb">
<head>
<meta charset="utf-8">
<title>'e Lendorf Glas Hunneg – Etikett</title>
<link rel="stylesheet" href="https://fonts.googleapis.com/css2?family=Montserrat:wght@300;400;600;700&display=swap">
<style>
  :root {
    --bg: #fcf2e8;
    --brown: #2e0e0c;
    --gold: #e9b23a;
    --gold-soft: #d49a2c;
    --gold-deep: #b9781c;
    --cream: #f6ead3;
    --white: #ffffff;
  }
  * { box-sizing: border-box; margin: 0; padding: 0; }
  html, body { width: 1200px; height: 753px; overflow: hidden; }
  body {
    background: var(--bg);
    font-family: "Montserrat", Arial, sans-serif;
    position: relative;
  }
  .sticker { position: absolute; left: 320px; top: 26px; width: 560px; height: 700px; }

  /* seal stripe over the lid */
  .seal-stripe {
    position: absolute; left: 160px; top: 0; width: 62px; height: 392px;
    background: var(--brown);
    border-left: 2px solid var(--gold-soft);
    border-right: 2px solid var(--gold-soft);
  }
  .seal-text {
    position: absolute; left: 50%; top: 22px; transform: translateX(-50%);
    writing-mode: vertical-rl;
    font-size: 17px; font-weight: 300; color: var(--cream); letter-spacing: 0.5px;
    white-space: nowrap;
  }
  .seal-comb {
    position: absolute; left: 0; right: 0; top: 250px; height: 110px;
    background: radial-gradient(circle at 55% 45%, var(--gold) 0%, var(--gold-soft) 45%, var(--brown) 100%);
  }

  /* main front label */
  .front-label {
    position: absolute; left: 0; top: 392px; width: 560px; height: 308px;
    background: var(--brown);
    overflow: hidden;
  }
  .comb-band { position: absolute; top: 0; bottom: 0; }
  .comb-band--left {
    left: 0; width: 66px;
    background: linear-gradient(180deg, var(--gold-soft), var(--gold) 40%, var(--gold-deep) 75%, var(--gold-soft));
  }
  .comb-band--right {
    right: 0; width: 74px;
    background: linear-gradient(180deg, var(--gold), var(--gold-deep) 35%, var(--gold) 70%, var(--gold-soft));
  }
  .gold-rule { position: absolute; top: 0; bottom: 0; width: 2px; background: var(--gold-soft); }
  .gold-rule--left { left: 66px; }
  .gold-rule--right { right: 74px; }

  .label-body { position: absolute; left: 90px; right: 92px; top: 0; bottom: 0; }
  .producer {
    position: absolute; left: 0; top: 22px;
    font-size: 7px; color: var(--cream); letter-spacing: 0.3px;
  }
  .quantity {
    position: absolute; right: 0; top: 44px;
    font-size: 14px; font-weight: 600; color: var(--white);
  }
  .lead-in {
    position: absolute; left: 0; top: 78px;
    font-size: 18px; font-weight: 300; line-height: 1; color: var(--cream);
  }
  .title {
    position: absolute; left: 0; top: 104px;
    font-size: 58px; font-weight: 300; line-height: 1; letter-spacing: 1px;
    color: var(--cream);
  }
  .subtitle {
    position: absolute; left: 0; top: 170px;
    font-size: 14px; font-weight: 300; color: var(--gold);
  }
  .description {
    position: absolute; left: 0; right: 6px; top: 196px;
    font-size: 9.5px; font-weight: 600; line-height: 1.35; color: var(--white);
  }
  .storage {
    position: absolute; left: 0; top: 262px;
    font-size: 9.5px; color: var(--gold); line-height: 1.5;
  }
  .storage .note { display: block; color: var(--white); }
  .best-before {
    position: absolute; right: 0; top: 258px; width: 92px;
    font-size: 6px; color: var(--cream);
  }
  .date-field {
    margin-top: 3px; height: 12px; border: 1px solid var(--cream);
  }
</style>
</head>
<body>
  <div class="sticker">
    <div class="seal-stripe">
      <div class="seal-comb" role="img" aria-label="Honeycomb pattern in gold tones"></div>
      <div class="seal-text">'e lendorf glas HUNNEG</div>
    </div>

    <section class="front-label">
      <div class="comb-band comb-band--left" role="img" aria-label="Honeycomb pattern in gold tones"></div>
      <div class="comb-band comb-band--right" role="img" aria-label="Honeycomb pattern in gold tones"></div>
      <div class="gold-rule gold-rule--left"></div>
      <div class="gold-rule gold-rule--right"></div>

      <div class="label-body">
        <p class="producer">Marc Lendorf, 38, rue Ferd Lusang, L-9241 Miersch</p>
        <p class="quantity">500 gr</p>
        <p class="lead-in">'e lendorf glas</p>
        <h1 class="title">HUNNEG</h1>
        <p class="subtitle">pure raw honey</p>
        <p class="description">Hunneg gëtt a klenge Quantitéiten aus lokalen Niew-estänn geernt. Well en 100% réi an net pasteuriséiert ass, späichert en natierlech nëtzlech Pollen an Enzymer.</p>
        <p class="storage">'dréchen, kill andäischterstockéieren'<span class="note">Net u Puppelcher ënner engem Joer</span></p>
        <div class="best-before">Am beschte virum:<div class="date-field"></div></div>
      </div>
    </section>
  </div>
</body>
</html>
```